Single Page Timetracking Dashboard Desktop App UI Design (Figma Link required)

Main Idea: a SaaS tool where employees can add their time and project in a playful way. There is a infographics and a list with tasks as well.

Based on the attached concept.png the brief is following:

- check the attached rough scribble
- add own ideas or change things if they add value
- Style: colourful, nerdy, professional saas, modern, beautiful, white space
- Quality expectation: inspiration1+2.png
- I will need a Figma link
- desktop only
- make something fresh and unique

Process:
I need to include 2-3 feedback rounds that will span probably around 7 days

Target Market(s)

Internal Business Tool for a Software Development Company

Industry/Entity Type

IT

Other font styles liked:
• Could be monospace, not a must though

Requirements
Must have
• At least one page; Figma Link to the design;
Nice to have
• Microinterations like drop-down, hover/active colors; functionality specifications
Should not have
• Mobile view

```html
<!DOCTYPE html>
<html lang="en">
<head>
<meta charset="utf-8">
<title>Kronly Timetracking Dashboard</title>
<link href="https://fonts.googleapis.com/css2?family=Montserrat:wght@400;500;600;700&display=swap" rel="stylesheet">
<style>
:root{
  --bg:#f4f5f7;
  --panel:#ffffff;
  --ink:#2b2f36;
  --muted:#6b7178;
  --faint:#c3c8ce;
  --line:#e6e8eb;
  --blue:#1b7bc2;
  --blue-soft:#6aa9ec;
  --bar-track:#e3effb;
  --bar:#6aa6e6;
  --green:#27a844;
  --yellow:#fcc443;
  --orange:#f7984a;
  --red:#bf4430;
  --chip:#f2f3f5;
}
*{box-sizing:border-box;margin:0;padding:0}
html,body{width:1200px;height:750px;overflow:hidden}
body{background:var(--bg);font-family:"Montserrat",sans-serif;color:var(--ink);position:relative}
.panel{position:absolute;background:var(--panel);border-radius:12px}
.abs{position:absolute}
/* sidebar */
.sidebar{left:13px;top:13px;width:107px;height:723px;text-align:center}
.brand{top:28px;left:0;width:100%;font-size:15px;font-weight:500;color:var(--ink);letter-spacing:1px}
.brand-rule{top:57px;left:13px;width:81px;height:1px;background:var(--line)}
.brand-sub{top:68px;left:0;width:100%;font-size:10.5px;line-height:13px;color:var(--ink)}
.nav-item{left:13px;width:81px;height:66px;border-radius:10px;font-size:10px;font-weight:500;color:#9aa0a6;display:flex;flex-direction:column;align-items:center;justify-content:center;gap:6px}
.nav-item svg{width:18px;height:18px;stroke:currentColor;fill:none;stroke-width:1.4}
.nav-item.active{background:var(--blue-soft);color:#fff;font-weight:600}
.logout{left:44px;top:686px;width:19px;height:19px;stroke:#8a9096;fill:none;stroke-width:1.4}
/* hero */
.hero{left:133px;top:13px;width:460px;height:160px;overflow:hidden;color:#fff}
.hero-bg{inset:0;background:linear-gradient(120deg,#3b4a5c 0%,#58718b 50%,#3e5064 100%)}
.hero-date{top:18px;width:100%;text-align:center;font-size:12px}
.hero-title{top:40px;width:100%;text-align:center;font-size:20px;font-weight:600}
.stat-card{top:82px;width:208px;height:61px;border-radius:6px;background:rgba(255,255,255,.16);display:flex;align-items:center;padding-left:14px;gap:14px}
.stat-card svg{width:34px;height:34px;stroke:#fff;fill:none;stroke-width:2}
.stat-value{font-size:14px;font-weight:600}
.stat-label{font-size:12px;margin-top:3px;opacity:.9}
/* filters */
.filters{left:133px;top:187px;width:460px;height:550px}
.panel-title{left:17px;top:18px;font-size:14px;font-weight:600}
.rule{height:1px;background:var(--line)}
.close{left:429px;top:19px;width:14px;height:14px;stroke:#9aa0a6;stroke-width:1.4}
.field-label{left:17px;font-size:10.5px;font-weight:600}
.option{left:110px;font-size:10.5px;display:flex;align-items:center;gap:7px;color:#3b4047}
.radio{width:13px;height:13px;border-radius:50%;border:1.3px solid var(--blue-soft)}
.radio.on{border:3.5px solid var(--blue)}
.check{width:13px;height:13px;border-radius:2px;background:var(--blue);display:flex;align-items:center;justify-content:center}
.check svg{width:9px;height:9px;stroke:#fff;stroke-width:2;fill:none}
.select{left:110px;width:333px;height:33px;border:1px solid var(--line);border-radius:4px;font-size:10.5px;padding-left:10px;display:flex;align-items:center}
.chev{position:absolute;right:10px;top:12px;width:9px;height:9px;stroke:var(--blue);stroke-width:1.5;fill:none}
.btn{height:33px;border-radius:17px;display:flex;align-items:center;justify-content:center;font-size:12px;font-weight:600}
.btn-ghost{border:1px solid var(--line);color:var(--blue-soft)}
.btn-primary{background:var(--blue);color:#fff}
.btn-disabled{background:#c9ccd0;color:#fff}
/* statistics */
.stats{left:607px;top:13px;width:300px;height:723px}
.link{font-size:10px}
.month{font-size:11.5px;font-weight:600;width:100%;text-align:center}
.nav-chev{width:10px;height:10px;fill:none;stroke-width:1.6}
.donut-total{left:0;top:185px;width:300px;text-align:center;font-size:20px;font-weight:500;line-height:26px}
.chip{width:130px;height:33px;border-radius:17px;background:var(--chip);display:flex;align-items:center;justify-content:space-between;padding:0 7px 0 10px;font-size:10px;font-weight:600}
.pill{font-size:9.5px;color:#fff;border-radius:9px;padding:3px 7px}
.cust{left:17px;width:267px}
.cust-row{display:flex;justify-content:space-between;font-size:10px}
.cust-row b{font-weight:600}
.bar{margin-top:9px;height:10px;border-radius:5px;background:var(--bar-track);overflow:hidden}
.bar span{display:block;height:100%;background:var(--bar);border-radius:5px}
/* track */
.track{left:920px;top:13px;width:267px;height:723px}
.calendar{left:17px;top:54px;width:233px;height:193px;border:1px solid var(--line);border-radius:4px}
.cal-grid{position:absolute;left:6px;top:50px;width:220px;display:grid;grid-template-columns:repeat(7,1fr);row-gap:4px;font-size:10px;text-align:center}
.cal-grid .dow{font-weight:600;margin-bottom:7px}
.cal-grid span{height:20px;line-height:20px}
.cal-grid .dim{color:#d5d9dd}
.cal-grid .today{background:#e3effb;color:var(--blue);border-radius:50%;width:22px;margin:0 auto}
.tselect{left:17px;width:233px;height:33px;border:1px solid var(--line);border-radius:4px;display:flex;font-size:10.5px}
.tselect .key{width:73px;background:#f2f3f5;display:flex;align-items:center;padding-left:10px}
.tselect .val{flex:1;display:flex;align-items:center;padding-left:10px;color:var(--faint);font-size:10px;position:relative}
.note{left:17px;top:385px;width:233px;height:125px;border:1px solid var(--line);border-radius:4px;padding:10px;font-size:10px;color:var(--faint)}
.dur{width:56px;height:34px;border:1px solid var(--blue);border-radius:4px;display:flex;align-items:center;justify-content:center;font-size:13px;color:#3b4047}
.dur.off{border-color:var(--line);color:#d5d9dd}
.and{left:17px;top:604px;width:233px;display:flex;align-items:center;gap:10px;font-size:9.5px;color:#b3b8be}
.and i{flex:1;height:1px;background:var(--line)}
</style>
</head>
<body>

<nav class="panel sidebar">
  <div class="abs brand">KRONLY</div>
  <div class="abs brand-rule"></div>
  <div class="abs brand-sub">Timetracking<br>Dashboard</div>
  <div class="abs nav-item active" style="top:237px">
    <svg viewBox="0 0 20 20"><path d="M3 9 10 3l7 6v8H3z"/><path d="M8 17v-5h4v5"/></svg>Home
  </div>
  <div class="abs nav-item" style="top:318px">
    <svg viewBox="0 0 20 20"><path d="M9 4a7 7 0 1 0 7 7H9z"/><path d="M12 1v7h7a7 7 0 0 0-7-7z"/></svg>Statistics
  </div>
  <div class="abs nav-item" style="top:398px">
    <svg viewBox="0 0 20 20"><rect x="4" y="3" width="12" height="15" rx="2"/><path d="M7 8h6M7 11h6M7 14h4M8 3V1h4v2"/></svg>Tasks
  </div>
  <div class="abs nav-item" style="top:478px">
    <svg viewBox="0 0 20 20"><circle cx="10" cy="6" r="3.5"/><path d="M3 18c0-4 3-6 7-6s7 2 7 6z"/></svg>Profile
  </div>
  <svg class="abs logout" viewBox="0 0 20 20"><path d="M8 3H3v14h5"/><path d="M7 10h11M14 6l4 4-4 4"/></svg>
</nav>

<header class="panel hero">
  <div class="abs hero-bg" role="img" aria-label="Photo of a notebook and pen on a desk in muted blue tones"></div>
  <div class="abs hero-date">Thursday, 26 Oct 2023</div>
  <div class="abs hero-title">Welcome, Sam Carter</div>
  <div class="abs stat-card" style="left:17px">
    <svg viewBox="0 0 34 34"><circle cx="17" cy="19" r="12"/><path d="M17 19v-6M14 4h6M17 4v3M27 9l2-2"/></svg>
    <div><div class="stat-value">9,876h 45m</div><div class="stat-label">Total Time</div></div>
  </div>
  <div class="abs stat-card" style="left:235px">
    <svg viewBox="0 0 34 34"><rect x="6" y="5" width="22" height="26" rx="3"/><path d="M12 5V3h10v2M11 13h2M16 13h8M11 19h2M16 19h8M11 25h2M16 25h8"/></svg>
    <div><div class="stat-value">345</div><div class="stat-label">Total Tasks</div></div>
  </div>
</header>

<section class="panel filters">
  <div class="abs panel-title">Filters</div>
  <svg class="abs close" viewBox="0 0 14 14"><path d="M1 1l12 12M13 1 1 13"/></svg>
  <div class="abs rule" style="left:17px;top:53px;width:426px"></div>

  <div class="abs field-label" style="top:71px">Period</div>
  <div class="abs option" style="top:71px"><span class="radio on"></span>This Week</div>
  <div class="abs option" style="top:94px"><span class="radio"></span>This Month</div>
  <div class="abs option" style="top:117px"><span class="radio"></span>This Quarter</div>
  <div class="abs option" style="top:140px"><span class="radio"></span>This Year</div>
  <div class="abs option" style="top:163px"><span class="radio"></span>Custom</div>

  <div class="abs field-label" style="top:204px">Type</div>
  <div class="abs select" style="top:194px">All<svg class="chev" viewBox="0 0 10 10"><path d="M1 3l4 4 4-4"/></svg></div>
  <div class="abs field-label" style="top:254px">Customer</div>
  <div class="abs select" style="top:244px">All<svg class="chev" viewBox="0 0 10 10"><path d="M1 3l4 4 4-4"/></svg></div>
  <div class="abs field-label" style="top:304px">Project</div>
  <div class="abs select" style="top:294px">All<svg class="chev" viewBox="0 0 10 10"><path d="M1 3l4 4 4-4"/></svg></div>

  <div class="abs field-label" style="top:344px">Time</div>
  <div class="abs option" style="top:344px"><span class="check"><svg viewBox="0 0 10 10"><path d="M2 5l2 2 4-4"/></svg></span>15m - 2h 45m</div>
  <div class="abs option" style="top:367px"><span class="check"><svg viewBox="0 0 10 10"><path d="M2 5l2 2 4-4"/></svg></span>3h - 4h 45m</div>
  <div class="abs option" style="top:390px"><span class="check"><svg viewBox="0 0 10 10"><path d="M2 5l2 2 4-4"/></svg></span>5h - 6h 45m</div>
  <div class="abs option" style="top:413px"><span class="check"><svg viewBox="0 0 10 10"><path d="M2 5l2 2 4-4"/></svg></span>7h - 8h 45m</div>

  <div class="abs btn btn-ghost" style="left:17px;top:500px;width:208px">Reset</div>
  <div class="abs btn btn-primary" style="left:235px;top:500px;width:208px">Apply Filters</div>
</section>

<section class="panel stats">
  <div class="abs panel-title" style="top:17px;font-size:17px">Statistics</div>
  <div class="abs link" style="left:159px;top:22px;color:var(--muted)">Monthly
    <svg style="width:9px;height:9px;margin-left:3px;stroke:var(--blue);stroke-width:1.5;fill:none" viewBox="0 0 10 10"><path d="M1 3l4 4 4-4"/></svg></div>
  <div class="abs" style="left:227px;top:18px;width:1px;height:20px;background:var(--line)"></div>
  <div class="abs link" style="left:241px;top:22px;color:var(--blue);font-weight:500">View All</div>
  <div class="abs rule" style="left:17px;top:53px;width:267px"></div>
  <svg class="abs nav-chev" style="left:20px;top:67px;stroke:var(--blue)" viewBox="0 0 10 10"><path d="M7 1 3 5l4 4"/></svg>
  <div class="abs month" style="top:66px">October 2023</div>
  <svg class="abs nav-chev" style="left:270px;top:67px;stroke:#d5d9dd" viewBox="0 0 10 10"><path d="M3 1l4 4-4 4"/></svg>
  <div class="abs rule" style="left:17px;top:91px;width:267px"></div>

  <svg class="abs" style="left:50px;top:109px" width="200" height="200" viewBox="0 0 200 200" aria-label="Share of tracked time by duration">
    <g transform="rotate(-90 100 100)" fill="none" stroke-width="29">
      <circle cx="100" cy="100" r="85.5" pathLength="100" stroke="var(--green)" stroke-dasharray="8.7 91.3" stroke-dashoffset="-0.15"/>
      <circle cx="100" cy="100" r="85.5" pathLength="100" stroke="var(--yellow)" stroke-dasharray="21.7 78.3" stroke-dashoffset="-9.15"/>
      <circle cx="100" cy="100" r="85.5" pathLength="100" stroke="var(--orange)" stroke-dasharray="37.7 62.3" stroke-dashoffset="-31.15"/>
      <circle cx="100" cy="100" r="85.5" pathLength="100" stroke="var(--red)" stroke-dasharray="30.7 69.3" stroke-dashoffset="-69.15"/>
    </g>
  </svg>
  <div class="abs donut-total">114h<br>30m</div>

  <div class="abs chip" style="left:17px;top:326px">15m - 2h 45m<span class="pill" style="background:var(--green)">9%</span></div>
  <div class="abs chip" style="left:153px;top:326px">3h - 4h 45m<span class="pill" style="background:var(--yellow)">22%</span></div>
  <div class="abs chip" style="left:17px;top:366px">5h - 6h 45m<span class="pill" style="background:var(--orange)">38%</span></div>
  <div class="abs chip" style="left:153px;top:366px">7h - 8h 45m<span class="pill" style="background:var(--red)">31%</span></div>
  <div class="abs rule" style="left:17px;top:414px;width:267px"></div>

  <div class="abs cust" style="top:432px"><div class="cust-row">Customer A<b>40h 45m (53%)</b></div><div class="bar"><span style="width:56%"></span></div></div>
  <div class="abs cust" style="top:479px"><div class="cust-row">Customer B<b>8h 15m (13%)</b></div><div class="bar"><span style="width:29%"></span></div></div>
  <div class="abs cust" style="top:526px"><div class="cust-row">Customer C<b>20h (34%)</b></div><div class="bar"><span style="width:41%"></span></div></div>
  <div class="abs cust" style="top:572px"><div class="cust-row">Customer D<b>40h 45m (53%)</b></div><div class="bar"><span style="width:56%"></span></div></div>
  <div class="abs cust" style="top:619px"><div class="cust-row">Customer E<b>8h 15m (13%)</b></div><div class="bar"><span style="width:29%"></span></div></div>
  <div class="abs cust" style="top:666px"><div class="cust-row">Customer F<b>20h (34%)</b></div><div class="bar"><span style="width:41%"></span></div></div>
</section>

<section class="panel track">
  <div class="abs panel-title" style="top:17px;font-size:17px">Track Your Time</div>
  <div class="abs calendar">
    <svg class="abs nav-chev" style="left:17px;top:13px;stroke:var(--blue)" viewBox="0 0 10 10"><path d="M7 1 3 5l4 4"/></svg>
    <div class="abs month" style="top:12px">October 2023</div>
    <svg class="abs nav-chev" style="left:205px;top:13px;stroke:#d5d9dd" viewBox="0 0 10 10"><path d="M3 1l4 4-4 4"/></svg>
    <div class="abs rule" style="left:0;top:37px;width:231px"></div>
    <div class="cal-grid">
      <span class="dow">Su</span><span class="dow">Mo</span><span class="dow">Tu</span><span class="dow">We</span><span class="dow">Th</span><span class="dow">Fr</span><span class="dow">Sa</span>
      <span>1</span><span>2</span><span>3</span><span>4</span><span>5</span><span>6</span><span>7</span>
      <span>8</span><span>9</span><span>10</span><span>11</span><span>12</span><span>13</span><span>14</span>
      <span>15</span><span>16</span><span>17</span><span>18</span><span>19</span><span>20</span><span>21</span>
      <span>22</span><span>23</span><span>24</span><span>25</span><span class="today">26</span><span class="dim">27</span><span class="dim">28</span>
      <span class="dim">29</span><span class="dim">30</span><span class="dim">31</span>
    </div>
  </div>

  <div class="abs tselect" style="top:265px"><div class="key">Type</div><div class="val">Select<svg class="chev" viewBox="0 0 10 10"><path d="M1 3l4 4 4-4"/></svg></div></div>
  <div class="abs tselect" style="top:305px"><div class="key">Customer</div><div class="val">Select<svg class="chev" viewBox="0 0 10 10"><path d="M1 3l4 4 4-4"/></svg></div></div>
  <div class="abs tselect" style="top:345px"><div class="key">Project</div><div class="val">Select<svg class="chev" viewBox="0 0 10 10"><path d="M1 3l4 4 4-4"/></svg></div></div>
  <div class="abs note">What did you do?</div>

  <div class="abs dur" style="left:17px;top:529px">1h</div>
  <div class="abs dur" style="left:76px;top:529px">2h</div>
  <div class="abs dur" style="left:135px;top:529px">3h</div>
  <div class="abs dur" style="left:194px;top:529px">4h</div>
  <div class="abs dur" style="left:17px;top:565px">5h</div>
  <div class="abs dur" style="left:76px;top:565px">6h</div>
  <div class="abs dur" style="left:135px;top:565px">7h</div>
  <div class="abs dur" style="left:194px;top:565px">8h</div>
  <div class="abs and"><i></i>and<i></i></div>
  <div class="abs dur off" style="left:17px;top:624px">0m</div>
  <div class="abs dur" style="left:76px;top:624px">15m</div>
  <div class="abs dur" style="left:135px;top:624px">30m</div>
  <div class="abs dur" style="left:194px;top:624px">45m</div>

  <div class="abs btn btn-ghost" style="left:17px;top:674px;width:111px">Clear</div>
  <div class="abs btn btn-disabled" style="left:138px;top:674px;width:112px">Save</div>
</section>

</body>
</html>
```